The Brightpath Scholar, an online college fair for non-traditional students, needs a web site

I need design and coding for a functioning web site that will serve as an online college fair that connects non-traditional students with college admissions officers and college advisors. I have chosen Wordpress and the "Meridian" theme for the site, and you can see what I already have here: https://brightpathscholar.example/
I need help setting up the site's pages and functionality, including SEO optimization and a password protected area. I will manage all content. In addition to me as the administrator, other users will be: college admissions officers, non-traditional students (like homeschoolers), and college advisors.
Target Market(s)
Homeschoolers and college/university admissions officers
Industry/Entity Type
College
Coding
Coded - Design and coding required
Number of Pages Required
5+ page
Requirements
Must have
- - An inviting but professional look (see the logo as a starting point)
- - Easy to navigate
- - A way to register subscribed members (students)
- - A password-protected "members only" area
- - Virtual "booths" on the Schools page that lead to a detail page for each school
- - SEO optimized
Nice to have
- - Searchable site

```html
<!DOCTYPE html>
<html lang="en">
<head>
<meta charset="utf-8">
<title>The Brightpath Scholar</title>
<link href="https://fonts.googleapis.com/css2?family=Open+Sans:wght@300;400;600;700&family=Lato:wght@400;700&display=swap" rel="stylesheet">
<style>
:root{
  --red:#e40b0b;
  --red-bright:#ff0000;
  --red-card:#e00808;
  --ink:#333;
  --muted:#777;
  --light:#999;
  --black:#000;
  --white:#fff;
  --line:#e6e6e6;
}
*{box-sizing:border-box;margin:0;padding:0}
html,body{width:1200px;height:1120px;overflow:hidden;background:var(--white)}
body{font-family:"Open Sans",Arial,sans-serif;color:var(--ink)}
.stage{position:absolute;left:0;top:0;width:1500px;height:1400px;transform:scale(.8);transform-origin:0 0}
.site{position:absolute;left:486px;top:0;width:528px;height:1400px;background:var(--white)}
.abs{position:absolute}

/* top bar */
.topbar{left:0;top:0;width:528px;height:14px;background:var(--red)}
.topbar-mail{left:30px;top:2px;font-size:7px;color:var(--white);display:flex;align-items:center;gap:4px}
.topbar-social{right:32px;top:3px;display:flex;gap:3px}
.topbar-social span{width:7px;height:7px;border-radius:1px;background:#ffb400}
.topbar-social span:nth-child(n+2){background:#5aa9e6}

/* header */
.brand{left:30px;top:20px;display:flex;align-items:center;gap:6px}
.brand-mark{width:22px;height:22px;background:var(--red)}
.brand-name{font-size:9px;font-weight:600;color:var(--ink);letter-spacing:.3px;line-height:1.1}
.brand-tag{font-size:3.5px;color:var(--muted);margin-top:2px}
.btn{top:27px;height:12px;background:var(--red);color:var(--white);font-size:5px;font-weight:600;display:flex;align-items:center;justify-content:center;border-radius:1px}
.btn-login{left:419px;width:37px}
.btn-register{left:460px;width:37px}

/* hero */
.hero{left:0;top:56px;width:528px;height:243px;background:linear-gradient(135deg,#c9cfc8 0%,#8a8a84 35%,#6b3a2c 60%,#3a3532 100%)}

/* audience cards */
.card{color:var(--white);text-align:center}
.card-side{top:239px;width:137px;height:179px;background:var(--red-card)}
.card-students{left:52px}
.card-colleges{left:337px;width:140px}
.card-advisors{left:189px;top:225px;width:148px;height:220px;background:var(--red-bright)}
.card-icon{position:absolute;left:50%;width:50px;height:50px;margin-left:-25px;border-radius:50%;background:var(--red-bright);border:2px solid rgba(255,255,255,.25);box-shadow:0 2px 4px rgba(0,0,0,.25);display:flex;align-items:center;justify-content:center}
.card-side .card-icon{top:-28px}
.card-advisors .card-icon{top:-25px;background:#e00808}
.card-title{font-size:7.5px;font-weight:700;line-height:8px;text-transform:uppercase}
.card-text{font-size:5.3px;line-height:11.5px;padding:0 10px;margin-top:8px}
.card-students .card-title{margin-top:25px}
.card-advisors .card-title{margin-top:48px}
.card-colleges .card-title{margin-top:28px}

/* intro */
.intro{left:50px;top:484px;width:428px;text-align:center}
.intro h2{font-weight:300;font-size:21px;color:var(--ink);letter-spacing:-.2px}
.intro h2 em{font-style:normal;color:var(--red)}
.intro p{font-size:5.2px;line-height:11.6px;color:var(--muted);margin-top:12px}
.intro p + p{margin-top:12px}

/* newsletter */
.newsletter{left:0;top:649px;width:528px;height:224px;background:linear-gradient(120deg,#2d2f33 0%,#45474b 45%,#2a2b2e 100%);text-align:center;color:var(--white)}
.newsletter h3{margin-top:58px;font-weight:300;font-size:21px;letter-spacing:.3px}
.newsletter p{font-size:5.5px;line-height:11.5px;margin:11px auto 0;width:270px}
.news-form{position:absolute;left:158px;top:132px;display:flex}
.news-input{width:179px;height:25px;background:rgba(255,255,255,.55);font-size:5.5px;color:#eee;text-align:left;padding:10px 12px}
.news-send{width:30px;height:25px;background:var(--red);display:flex;align-items:center;justify-content:center}

/* news */
.news{font-family:"Lato","Open Sans",sans-serif}
.news-heading{left:47px;top:916px;font-size:14px;font-weight:400;color:#444}
.feature-media{left:47px;top:942px;width:220px;height:170px;background:linear-gradient(150deg,#e8eef1 0%,#b9c6cc 45%,#7e8a90 100%);border-bottom:3px solid var(--red)}
.feature-title{left:47px;top:1121px;width:220px;font-size:12px;font-weight:400;color:#444;padding-bottom:4px;border-bottom:1px solid var(--line)}
.meta{font-size:7px;color:var(--light);display:flex;align-items:center;gap:6px}
.meta .likes,.meta .comments{display:flex;align-items:center;gap:2px}
.meta .num{color:var(--red)}
.feature-meta{left:47px;top:1145px}
.feature-text{left:47px;top:1162px;width:222px;font-size:7.6px;line-height:14.5px;color:#7a6d60}
.news-item{left:276px;width:212px;height:52px}
.item-thumb{position:absolute;left:0;top:0;width:66px;height:50px;border-right:2px solid var(--red)}
.item-title{position:absolute;left:73px;top:3px;width:140px;font-size:8px;line-height:12.5px;color:#444;font-weight:700}
.item-meta{position:absolute;left:73px}
.item-rule{position:absolute;left:73px;width:139px;border-top:1px solid var(--line)}

/* footer */
.footer-rule{left:0;top:1218px;width:528px;height:7px;background:var(--red)}
.footer{left:0;top:1225px;width:528px;height:175px;background:var(--black);color:var(--white)}
.footer-brand{position:absolute;left:50px;top:36px;width:104px;display:flex;flex-direction:column;align-items:center;gap:8px;text-align:center}
.footer-brand-mark{width:40px;height:40px;background:var(--red)}
.footer-brand-name{font-size:10px;line-height:12px;font-weight:600;color:var(--white)}
.footer-col{position:absolute;top:36px}
.footer-col h4{font-size:7px;font-weight:700;letter-spacing:.2px}
.footer-list{list-style:none;margin-top:14px;font-size:4.8px;line-height:14px}
.contact-list li{display:flex;gap:4px;align-items:flex-start;line-height:9px;margin-bottom:9px}
.contact-list svg{flex:none;margin-top:1px}
.col-contact{left:172px;width:100px}
.col-links{left:279px}
.links-grid{display:grid;grid-template-columns:46px 46px}
.col-follow{left:394px}
.follow-icons{display:flex;gap:3px;margin-top:14px}
.follow-icons span{width:9px;height:9px;border-radius:1px;background:#3b6fc4}
.follow-icons span:nth-child(3),.follow-icons span:nth-child(4){background:#d93a2b}
.footer-line{position:absolute;left:50px;top:150px;width:427px;border-top:1px solid #333}
.copyright{position:absolute;left:0;width:528px;top:157px;text-align:center;font-size:5.3px;color:#ccc}
</style>
</head>
<body>
<div class="stage">
<div class="site">

  <div class="abs topbar"></div>
  <div class="abs topbar-mail">
    <svg width="7" height="5" viewBox="0 0 7 5"><rect x=".5" y=".5" width="6" height="4" fill="none" stroke="#fff" stroke-width=".8"/><path d="M.5 .5 3.5 3 6.5 .5" fill="none" stroke="#fff" stroke-width=".8"/></svg>
    hello@brightpathscholar.example
  </div>
  <div class="abs topbar-social"><span></span><span></span><span></span><span></span><span></span></div>

  <header>
    <div class="abs brand">
      <div class="brand-mark"></div>
      <div>
        <div class="brand-name">The Brightpath Scholar</div>
        <div class="brand-tag">A virtual college fair for non-traditional students</div>
      </div>
    </div>
    <div class="abs btn btn-login">LOGIN</div>
    <div class="abs btn btn-register">REGISTER</div>
  </header>

  <div class="abs hero" role="img" aria-label="Photo of students meeting with an admissions advisor around an office desk"></div>

  <section class="abs card card-side card-students">
    <div class="card-icon">
      <svg width="30" height="18" viewBox="0 0 30 18" fill="#fff"><circle cx="7" cy="6" r="3"/><path d="M2 16c0-4 2-6 5-6s5 2 5 6z"/><circle cx="15" cy="5" r="3.4"/><path d="M9.5 16c0-4.5 2.5-7 5.5-7s5.5 2.5 5.5 7z"/><circle cx="23" cy="6" r="3"/><path d="M18 16c0-4 2-6 5-6s5 2 5 6z"/></svg>
    </div>
    <div class="card-title">For Students</div>
    <p class="card-text">free membership for any student or parent who wants to learn more about the colleges and universities that are actively recruiting non-traditional students, all in one location! You will have access to admissions officers, independent admissions advisors, regular articles on higher education topics, and resource reviews and links. We will also offer regular events, like webinars and admissions panels, where you can interact directly with admissions officers, college advisors</p>
  </section>

  <section class="abs card card-advisors">
    <div class="card-icon">
      <svg width="20" height="20" viewBox="0 0 20 20" fill="#fff"><circle cx="10" cy="6" r="4.5"/><path d="M2 19c0-5 3.5-7.5 8-7.5s8 2.5 8 7.5z"/></svg>
    </div>
    <div class="card-title">For Independent<br>College Advisors</div>
    <p class="card-text">... a platform for sharing your services and connecting with thousands of students who need your guidance. Through forums, articles, ads, and online events, there will be multiple opportunities to share your knowledge and expertise, and to work closely with individual students</p>
  </section>

  <section class="abs card card-side card-colleges">
    <div class="card-icon">
      <svg width="24" height="18" viewBox="0 0 24 18" fill="#fff"><path d="M12 1 23 6 12 11 1 6z"/><path d="M6 9v5c2 2 10 2 12 0V9l-6 3z"/><rect x="21" y="6" width="1.2" height="7"/></svg>
    </div>
    <div class="card-title">For Colleges and<br>Universities</div>
    <p class="card-text">an audience of thousands of non-traditional students who want to hear about your school and programs. You will have a dedicated page to set up a virtual "booth", or school profile, where you can describe your institution, highlight aspects of your programs that may appeal to non-traditional students, offer details of their admissions process and requirements, and provide contact information for designated admissions</p>
  </section>

  <section class="abs intro">
    <h2>YOUR HEADING <em>GOES HERE</em></h2>
    <p>Lorem Ipsum is simply dummy text of the printing and typesetting industry. Lorem Ipsum has been the industry's standard dummy text ever since the 1500s, when an unknown printer took a galley of type and scrambled it to make a type specimen book. It has survived not only five centuries Lorem Ipsum is simply dummy text of the printing and typesetting industry. Lorem Ipsum has been the industry's standard dummy text ever since the 1500s, when an unknown printer took a galley of type and scrambled it to make a type specimen book. It has survived not only five centurie</p>
    <p>Lorem Ipsum is simply dummy text of the printing and typesetting industry. Lorem Ipsum has been the industry's standard dummy text ever since the 1500s, when an unknown printer took a galley of type and scrambled it to make a type specimen book. It has survived not only five centuries Lorem Ipsum is simply dummy text of the printing and typesetting industry. Lorem Ipsum has been the industry's standard</p>
  </section>

  <section class="abs newsletter" role="img" aria-label="Darkened photo of students studying in a classroom, behind the newsletter signup">
    <h3>NEWSLETTER</h3>
    <p>Lorem Ipsum is simply dummy text of the printing and typesetting industry. Lorem Ipsum has been the industry's standard dummy text ever since the 1500s.</p>
    <div class="news-form">
      <div class="news-input">Email</div>
      <div class="news-send">
        <svg width="11" height="11" viewBox="0 0 11 11"><path d="M10 1 1 5l4 1.5L6.5 10z" fill="none" stroke="#fff" stroke-width=".9" stroke-linejoin="round"/><path d="M10 1 5 6.5" stroke="#fff" stroke-width=".9"/></svg>
      </div>
    </div>
  </section>

  <section class="news">
    <h3 class="abs news-heading">Latest news</h3>
    <div class="abs feature-media" role="img" aria-label="Photo of hands typing on a laptop showing analytics charts"></div>
    <h4 class="abs feature-title">Ut in laoreet sapien eu amet</h4>
    <div class="abs meta feature-meta">
      <span>◷ December 14, 2015</span>
      <span class="likes">♡ 88</span>
      <span class="comments">▭ <span class="num">0</span></span>
    </div>
    <p class="abs feature-text">Penatibus et magnis dis parturient montes, nascetur ridiculus mus. Etiam ultrices metus ut enim biben dum, vitae fringilla diam mattis. Sed eget lacus.</p>

    <article class="abs news-item" style="top:942px">
      <div class="item-thumb" role="img" aria-label="Photo of a person seated with a coffee cup" style="background:linear-gradient(135deg,#7a8b94,#b08a6a)"></div>
      <h5 class="item-title">Nam nec felis et nibh posuere</h5>
      <div class="item-rule" style="top:20px"></div>
      <div class="meta item-meta" style="top:24px"><span>◷ December 14, 2015</span><span class="likes">♡ 102</span><span class="comments">▭ <span class="num">0</span></span></div>
    </article>
    <article class="abs news-item" style="top:1005px">
      <div class="item-thumb" role="img" aria-label="Photo of a person relaxing in a chair by the sea" style="background:linear-gradient(180deg,#b8d3e6,#9a6a44)"></div>
      <h5 class="item-title">Aenean sodales pretium nullam</h5>
      <div class="item-rule" style="top:20px"></div>
      <div class="meta item-meta" style="top:24px"><span>◷ December 14, 2015</span><span class="likes">♡ 44</span><span class="comments">▭ <span class="num">0</span></span></div>
    </article>
    <article class="abs news-item" style="top:1068px">
      <div class="item-thumb" role="img" aria-label="Photo of a hand over papers on a desk" style="background:linear-gradient(135deg,#3a3d42,#c9cdd2)"></div>
      <h5 class="item-title">Vestibulum at pulvinar nullam</h5>
      <div class="item-rule" style="top:20px"></div>
      <div class="meta item-meta" style="top:24px"><span>◷ December 14, 2015</span><span class="likes">♡ 28</span><span class="comments">▭ <span class="num">0</span></span></div>
    </article>
    <article class="abs news-item" style="top:1131px">
      <div class="item-thumb" role="img" aria-label="Photo of a breakfast table with bread and cups" style="background:linear-gradient(135deg,#e9e2d2,#8a6a3c)"></div>
      <h5 class="item-title">Maecenas augue nunc cras habitasse</h5>
      <div class="item-rule" style="top:33px"></div>
      <div class="meta item-meta" style="top:36px"><span>◷ December 14, 2015</span><span class="likes">♡ 97</span><span class="comments">▭ <span class="num">0</span></span></div>
    </article>
  </section>

  <div class="abs footer-rule"></div>
  <footer class="abs footer">
    <div class="footer-brand">
      <div class="footer-brand-mark"></div>
      <div class="footer-brand-name">The Brightpath<br>Scholar</div>
    </div>

    <div class="footer-col col-contact">
      <h4>CONTACT DETAILS</h4>
      <ul class="footer-list contact-list">
        <li><svg width="5" height="5" viewBox="0 0 5 5"><path d="M1 0 2 1.3 1.4 2a3 3 0 0 0 1.6 1.6L3.7 3 5 4 4.2 5C2 5 0 3 0 .8z" fill="#fff"/></svg>0300 555 0142</li>
        <li><svg width="5" height="5" viewBox="0 0 5 5"><path d="M5 0 0 2l2 1 1 2z" fill="#fff"/></svg>contact@brightpathscholar.example</li>
        <li><svg width="5" height="6" viewBox="0 0 5 6"><path d="M2.5 6C1 4 0 3 0 2a2.5 2.5 0 0 1 5 0c0 1-1 2-2.5 4z" fill="#fff"/><circle cx="2.5" cy="2" r=".8" fill="#000"/></svg><span>12 Maple Lane<br>Riverside Town</span></li>
      </ul>
    </div>

    <div class="footer-col col-links">
      <h4>QUICK LINK</h4>
      <ul class="footer-list links-grid">
        <li>HOME</li><li>RESOURCES</li>
        <li>STUDENTS</li><li>NEWS</li>
        <li>SCHOOLS</li><li>CONTACT US</li>
        <li>ADVISORS</li><li></li>
        <li>MEMBER</li>
      </ul>
    </div>

    <div class="footer-col col-follow">
      <h4>FOLLOW US ON</h4>
      <div class="follow-icons"><span></span><span></span><span></span><span></span><span></span></div>
    </div>

    <div class="footer-line"></div>
    <p class="copyright">Copyright © 2017 Brightpath Scholar. All rights reserved</p>
  </footer>

</div>
</div>
</body>
</html>
```